Design a Mobile App for Landscape Businesses

This project is to design the first three screens for a mobile app for Landscape and Lawncare businesses. This app will serve as a directory for homeowners to locate landscape and lawn care businesses and for landscape businesses and contractors to run their business. See the attached PDF for more information and example
Here is the link to the description https://brevlinq.test/k3r92P

Target Market(s)

Landscape and lawn care business, gardeners, home owners

Industry/Entity Type

Landscape Gardening

Logo Text

Quillmoray

Colors

Designer to choose colors to be used in the design.

```html
<!DOCTYPE html>
<html lang="en">
<head>
<meta charset="utf-8">
<title>Quillmoray – Sign up</title>
<link href="https://fonts.googleapis.com/css2?family=Montserrat:wght@400;500;600;700&display=swap" rel="stylesheet">
<style>
  :root {
    --backdrop-top: #6f7d77;
    --backdrop-mid: #56655e;
    --backdrop-low: #4b5a4a;
    --backdrop-bloom: #6a5a86;
    --shade: rgba(30, 40, 38, 0.45);
    --text-light: #ffffff;
    --circle-blue: #2d6cb7;
    --chirp-start: #1f9ad6;
    --chirp-end: #22c6d5;
    --field-bg: #ffffff;
    --field-text: #3a3a3a;
    --field-icon: #2bb3d1;
    --email-green: #3ba73b;
    --divider: rgba(255, 255, 255, 0.55);
  }
  * { box-sizing: border-box; margin: 0; padding: 0; }
  html, body { width: 675px; height: 1200px; overflow: hidden; background: #000; }
  body { font-family: "Montserrat", Arial, sans-serif; color: var(--text-light); }

  .screen { position: relative; width: 675px; height: 1200px; overflow: hidden; }

  .backdrop-photo {
    position: absolute; inset: 0;
    background:
      radial-gradient(ellipse at 20% 92%, var(--backdrop-bloom) 0%, transparent 40%),
      radial-gradient(ellipse at 80% 85%, #5e7b4a 0%, transparent 45%),
      linear-gradient(180deg, var(--backdrop-top) 0%, var(--backdrop-mid) 45%, var(--backdrop-low) 100%);
  }
  .backdrop-shade { position: absolute; inset: 0; background: var(--shade); }

  .status-bar {
    position: absolute; top: 0; left: 0; right: 0; height: 43px;
    display: flex; justify-content: flex-end; align-items: center;
    gap: 10px; padding-right: 22px; font-size: 22px; font-weight: 500;
  }
  .status-bar svg { display: block; }

  .brand { position: absolute; top: 126px; left: 0; right: 0; text-align: center; }
  .brand-dot {
    width: 84px; height: 84px; margin: 0 auto 20px;
    border: 4px solid var(--text-light); border-radius: 50%;
  }
  .brand-name { font-size: 40px; font-weight: 700; line-height: 1; }
  .brand-tag { margin-top: 14px; font-size: 19px; font-weight: 500; letter-spacing: 12px; padding-left: 12px; }
  .tagline { position: absolute; top: 352px; left: 0; right: 0; text-align: center; font-size: 30px; font-weight: 500; }
  .login-prompt { position: absolute; top: 468px; left: 0; right: 0; text-align: center; font-size: 23px; }
  .login-prompt strong { font-weight: 700; }

  .button {
    position: absolute; left: 22px; width: 635px; height: 81px; border-radius: 5px;
    display: flex; justify-content: center; align-items: center; gap: 16px;
    font-size: 23px; font-weight: 700;
  }
  .button-mark { width: 28px; height: 28px; background: var(--text-light); border-radius: 50%; }
  .button-circlepage { top: 583px; background: var(--circle-blue); }
  .button-chirplane { top: 682px; background: linear-gradient(90deg, var(--chirp-start), var(--chirp-end)); }
  .button-email { top: 1098px; background: var(--email-green); font-size: 22px; }

  .divider { position: absolute; top: 812px; left: 29px; width: 615px; height: 2px; background: var(--divider); }

  .field {
    position: absolute; left: 29px; width: 619px; height: 81px; border-radius: 4px;
    background: var(--field-bg); color: var(--field-text);
    display: flex; align-items: center; gap: 16px; padding-left: 28px; font-size: 24px;
  }
  .field-email { top: 853px; }
  .field-password { top: 958px; }
</style>
</head>
<body>
<main class="screen">
  <div class="backdrop-photo" role="img" aria-label="Photo of a gardener watering flowers with a watering can"></div>
  <div class="backdrop-shade"></div>

  <div class="status-bar">
    <svg width="22" height="22" viewBox="0 0 22 22" aria-hidden="true"><circle cx="11" cy="12" r="8" fill="none" stroke="#fff" stroke-width="2.4"/><path d="M11 8v4l3 2" stroke="#fff" stroke-width="2.2" fill="none"/></svg>
    <svg width="26" height="22" viewBox="0 0 26 22" aria-hidden="true"><path d="M13 20L1 6a18 18 0 0 1 24 0z" fill="#fff"/></svg>
    <svg width="22" height="22" viewBox="0 0 22 22" aria-hidden="true"><path d="M2 20L20 2v18z" fill="#fff"/></svg>
    <svg width="14" height="24" viewBox="0 0 14 24" aria-hidden="true"><rect x="4" y="0" width="6" height="3" fill="#fff"/><rect x="0" y="3" width="14" height="21" rx="2" fill="#fff"/></svg>
    <span>16:54</span>
  </div>

  <header class="brand">
    <div class="brand-dot"></div>
    <h1 class="brand-name">Quillmoray</h1>
    <p class="brand-tag">LOGO TBC</p>
  </header>

  <p class="tagline">On demand gardening services</p>
  <p class="login-prompt">Already have an account? <strong>Log in</strong></p>

  <div class="button button-circlepage"><span class="button-mark"></span>Sign up with Circlepage</div>
  <div class="button button-chirplane"><span class="button-mark"></span>Sign up with Chirplane</div>

  <div class="divider"></div>

  <div class="field field-email">
    <svg width="28" height="20" viewBox="0 0 28 20" aria-hidden="true"><rect x="1.5" y="1.5" width="25" height="17" rx="2" fill="none" stroke="var(--field-icon)" stroke-width="2.5"/><path d="M2 3l12 9 12-9" fill="none" stroke="var(--field-icon)" stroke-width="2.5"/></svg>
    <span>Email address</span>
  </div>
  <div class="field field-password">
    <svg width="22" height="28" viewBox="0 0 22 28" aria-hidden="true"><path d="M5 12V8a6 6 0 0 1 12 0v4" fill="none" stroke="var(--field-icon)" stroke-width="3"/><rect x="1" y="12" width="20" height="15" rx="2" fill="var(--field-icon)"/></svg>
    <span>Password</span>
  </div>

  <div class="button button-email">Sign up with Email address</div>
</main>
</body>
</html>
```